Morvane Art

A website showing drawings, thumbnails and full size with space for asize and adescription . With the ability to expand for more pictures and purchase through Quidora online. I already own www.morvaneart.com

```html
<!DOCTYPE html>
<html lang="en">
<head>
<meta charset="utf-8">
<title>Morvane Art</title>
<link href="https://fonts.googleapis.com/css2?family=Lato:wght@400;700;900&display=swap" rel="stylesheet">
<style>
:root{
  --orange:#f7941d;
  --ink:#333333;
  --muted:#777777;
  --dark:#2b2b2b;
  --darker:#1f1f1f;
  --light:#f3f3f3;
  --line:#e2e2e2;
  --white:#ffffff;
}
*{box-sizing:border-box;margin:0;padding:0}
html,body{width:1200px;height:2620px;overflow:hidden}
body{font-family:"Lato",sans-serif;color:var(--ink);background:var(--white)}
.site-header{height:80px;display:flex;align-items:center;justify-content:space-between;padding:0 40px 0 32px;background:var(--white)}
.brand{font-size:30px;font-weight:900;letter-spacing:1px;color:var(--ink)}
.main-nav{display:flex;align-items:center;gap:6px}
.main-nav a{font-size:12px;font-weight:700;color:var(--ink);text-decoration:none;padding:10px 14px;text-transform:uppercase}
.main-nav a.active{background:var(--orange);color:var(--white)}
.cart{display:flex;align-items:center;gap:6px}
.hero{position:relative;height:580px;background:linear-gradient(135deg,#b9c3cf 0%,#7f8ea6 35%,#d8d2c8 60%,#5f6f8f 100%)}
.hero-text{position:absolute;left:64px;top:190px;padding:20px 28px 28px;background:rgba(0,0,0,.35);width:560px}
.hero-title{font-size:60px;font-weight:900;color:var(--white);letter-spacing:1px;line-height:1}
.hero-sub{font-size:26px;font-weight:700;color:var(--white);margin-top:12px;line-height:1.15}
.btn{display:inline-block;background:var(--orange);color:var(--white);font-size:12px;font-weight:700;text-transform:uppercase;padding:12px 22px;text-decoration:none}
.hero .btn{margin-top:20px}
.dots{position:absolute;left:50%;bottom:26px;transform:translateX(-50%);display:flex;gap:8px}
.dots span{width:12px;height:12px;border-radius:50%;background:rgba(255,255,255,.6)}
.dots span.on{background:var(--white)}
.featured{height:1000px;padding-top:62px}
.section-title{text-align:center;font-size:28px;font-weight:900;text-transform:uppercase;color:var(--ink)}
.rule{width:60px;height:3px;background:var(--orange);margin:10px auto 0}
.grid{display:grid;grid-template-columns:repeat(4,240px);gap:30px 32px;justify-content:center;margin-top:30px}
.card{background:var(--white);box-shadow:0 1px 6px rgba(0,0,0,.15);padding:12px 12px 16px;text-align:center}
.thumb{width:100%}
.row-a .thumb{height:190px}
.row-b .thumb{height:260px}
.card h3{font-size:14px;font-weight:900;text-transform:uppercase;margin-top:14px}
.size{font-size:12px;color:var(--muted);margin-top:6px}
.desc{font-size:12px;color:var(--muted);margin-top:8px;line-height:1.45}
.buy{display:flex;align-items:center;justify-content:center;margin:12px auto 0;width:180px;height:36px;background:var(--orange);font-size:12px;font-weight:700;color:var(--white);text-transform:uppercase;text-decoration:none}
.about-band{height:320px;background:var(--dark);color:var(--white);display:flex;gap:60px;padding:44px 72px 0}
.about-band h2{font-size:26px;font-weight:900;text-transform:uppercase}
.about,.testimonials{flex:1}
.band-text{font-size:13px;line-height:1.6;color:#cfcfcf;margin-top:18px}
.about .btn{margin-top:24px}
.t-head{display:flex;justify-content:space-between;align-items:center}
.arrows{display:flex;gap:14px}
.quote{display:flex;gap:18px;margin-top:18px}
.quote svg{flex:none}
.quote .band-text{margin-top:0}
.name{color:var(--orange);font-size:12px;font-weight:700;text-transform:uppercase;margin:16px 0 0 44px}
.social-feed{height:340px;padding-top:64px}
.feed-title{font-size:24px}
.feed{display:flex;gap:8px;justify-content:center;margin-top:34px}
.feed div{width:205px;height:188px}
.site-footer{height:260px;background:var(--light);display:flex;gap:40px;padding:34px 72px 0}
.col{width:190px}
.col h4,.newsletter h4{font-size:12px;font-weight:900;color:var(--orange);text-transform:uppercase;margin-bottom:10px}
.col a{display:block;font-size:12px;color:var(--ink);text-decoration:none;line-height:1.6}
.newsletter{flex:1}
.newsletter p{font-size:12px;color:var(--muted)}
.subscribe{display:flex;margin-top:14px}
.subscribe span{flex:1;height:40px;background:var(--white);border:1px solid var(--line);font-size:12px;color:#999;padding:12px}
.subscribe b{width:44px;height:40px;background:var(--darker);display:flex;align-items:center;justify-content:center}
.icons{display:flex;gap:14px;margin-top:22px;align-items:center}
.icons i{width:20px;height:20px;border-radius:50%;background:#8a8a8a;display:block}
.cards{display:flex;gap:8px;margin-top:16px;justify-content:flex-end}
.cards i{width:36px;height:22px;border-radius:3px;background:#9a9a9a;display:block}
.copyright{height:40px;background:var(--darker);color:#bbbbbb;font-size:12px;display:flex;align-items:center;padding:0 72px}
</style>
</head>
<body>
<header class="site-header">
  <div class="brand">MORVANE ART</div>
  <nav class="main-nav">
    <a class="active" href="#">Home</a>
    <a href="#">About Us</a>
    <a href="#">Drawings</a>
    <a href="#">Gallery</a>
    <a href="#">News</a>
    <a href="#">Contact</a>
    <a class="cart" href="#"><svg width="14" height="14" viewBox="0 0 14 14"><path d="M1 2h2l2 7h7l1-5H4" fill="none" stroke="#333" stroke-width="1.5"/><circle cx="6" cy="12" r="1.2" fill="#333"/><circle cx="11" cy="12" r="1.2" fill="#333"/></svg>My Cart (0)</a>
  </nav>
</header>

<section class="hero" role="img" aria-label="Colored pencil drawing of a classic car in a blue and white scene">
  <div class="hero-text">
    <div class="hero-title">MORVANE ART</div>
    <div class="hero-sub">Cras magna ex euismod id risus sit amet pretium mollis odio.</div>
    <a class="btn" href="#">Shop Now</a>
  </div>
  <div class="dots"><span class="on"></span><span></span><span></span><span></span></div>
</section>

<section class="featured">
  <h2 class="section-title">Featured Drawings</h2>
  <div class="rule"></div>
  <div class="grid">
    <article class="card row-a"><div class="thumb" role="img" aria-label="Drawing of a vintage car" style="background:linear-gradient(135deg,#d8d0c4,#8d98a8)"></div><h3>Product Heading</h3><p class="size">9.8" x 11.0"</p><p class="desc">Curabitur pellentesque risus dui bibendum sit.</p><a class="buy" href="#">Buy now with Quidora</a></article>
    <article class="card row-a"><div class="thumb" role="img" aria-label="Colorful drawing of a hot rod" style="background:linear-gradient(135deg,#4f8f6a,#c64b5a)"></div><h3>Product Heading</h3><p class="size">9.8" x 11.0"</p><p class="desc">Curabitur pellentesque risus dui bibendum sit.</p><a class="buy" href="#">Buy now with Quidora</a></article>
    <article class="card row-a"><div class="thumb" role="img" aria-label="Drawing of a blue truck" style="background:linear-gradient(135deg,#3f7fb0,#7d5aa0)"></div><h3>Product Heading</h3><p class="size">9.8" x 11.0"</p><p class="desc">Curabitur pellentesque risus dui bibendum sit.</p><a class="buy" href="#">Buy now with Quidora</a></article>
    <article class="card row-a"><div class="thumb" role="img" aria-label="Yellow drawing of a car" style="background:linear-gradient(135deg,#f2cf3a,#e39a2b)"></div><h3>Product Heading</h3><p class="size">9.8" x 11.0"</p><p class="desc">Curabitur pellentesque risus dui bibendum sit.</p><a class="buy" href="#">Buy now with Quidora</a></article>
    <article class="card row-b"><div class="thumb" role="img" aria-label="Drawing of a purple muscle car" style="background:linear-gradient(135deg,#6a4c8c,#3d3d5c)"></div><h3>Product Heading</h3><p class="size">9.8" x 11.0"</p><p class="desc">Curabitur pellentesque risus dui bibendum sit.</p><a class="buy" href="#">Buy now with Quidora</a></article>
    <article class="card row-b"><div class="thumb" role="img" aria-label="Drawing of a car on blue sky" style="background:linear-gradient(135deg,#4d8ec4,#c85a3c)"></div><h3>Product Heading</h3><p class="size">9.8" x 11.0"</p><p class="desc">Curabitur pellentesque risus dui bibendum sit.</p><a class="buy" href="#">Buy now with Quidora</a></article>
    <article class="card row-b"><div class="thumb" role="img" aria-label="Drawing of a green sports car" style="background:linear-gradient(135deg,#5d9a55,#2f4f3a)"></div><h3>Product Heading</h3><p class="size">9.8" x 11.0"</p><p class="desc">Curabitur pellentesque risus dui bibendum sit.</p><a class="buy" href="#">Buy now with Quidora</a></article>
    <article class="card row-b"><div class="thumb" role="img" aria-label="Drawing of a red racing car" style="background:linear-gradient(135deg,#c8c4d6,#b33a3a)"></div><h3>Product Heading</h3><p class="size">9.8" x 11.0"</p><p class="desc">Curabitur pellentesque risus dui bibendum sit.</p><a class="buy" href="#">Buy now with Quidora</a></article>
  </div>
</section>

<section class="about-band">
  <div class="about">
    <h2>About Morvane Art</h2>
    <p class="band-text">Lorem ipsum dolor sit amet, consectetur adipiscing elit. Maecenas bibendum felis eget mattis mattis. Duis eu finibus arcu. Pellentesque gravida tortor eu velit fringilla rutrum et ut enim. Vivamus tincidunt augue sit amet iacus pulvinar placerat. In aliquam turpis sapien, sed posuere risus bibendum sit amet.</p>
    <a class="btn" href="#">Read More</a>
  </div>
  <div class="testimonials">
    <div class="t-head"><h2>Testimonials</h2>
      <div class="arrows"><svg width="10" height="14" viewBox="0 0 10 14"><path d="M8 1L2 7l6 6" fill="none" stroke="#fff" stroke-width="2.5"/></svg><svg width="10" height="14" viewBox="0 0 10 14"><path d="M2 1l6 6-6 6" fill="none" stroke="#fff" stroke-width="2.5"/></svg></div>
    </div>
    <div class="quote">
      <svg width="26" height="22" viewBox="0 0 26 22"><path d="M0 12Q0 2 10 0v4Q5 5 5 10h5v12H0zM14 12Q14 2 24 0v4Q19 5 19 10h5v12H14z" fill="#ffffff"/></svg>
      <p class="band-text">Lorem ipsum dolor sit amet, consectetur adipiscing elit. Maecenas bibendum felis eget mattis mattis. Duis eu finibus arcu. Pellentesque gravida tortor eu velit fringilla rutrum et ut enim. Vivamus tincidunt augue sit amet iacus pulvinar placerat...</p>
    </div>
    <p class="name">Name Heading</p>
  </div>
</section>

<section class="social-feed">
  <h2 class="section-title feed-title">@ Snapfeed</h2>
  <div class="feed">
    <div role="img" aria-label="Photo of a drawing in progress" style="background:linear-gradient(135deg,#8c8c8c,#3a3a3a)"></div>
    <div role="img" aria-label="Photo of a car drawing" style="background:linear-gradient(135deg,#b0a7b8,#6b5e78)"></div>
    <div role="img" aria-label="Photo of a colored car drawing" style="background:linear-gradient(135deg,#c6a35a,#6f7f52)"></div>
    <div role="img" aria-label="Photo of a pencil sketch" style="background:linear-gradient(135deg,#9fb0a4,#5c6e66)"></div>
    <div role="img" aria-label="Photo of a purple car drawing" style="background:linear-gradient(135deg,#8c6fb0,#c86fa0)"></div>
  </div>
</section>

<footer class="site-footer">
  <div class="col"><h4>Site Map</h4><a href="#">Home</a><a href="#">About Us</a><a href="#">Drawings</a><a href="#">Product</a><a href="#">Shop</a><a href="#">Blog</a><a href="#">Contact</a></div>
  <div class="col"><h4>Drawings</h4><a href="#">Curabitur</a><a href="#">Pellentesque risus</a><a href="#">Dolupis</a><a href="#">Placerat</a></div>
  <div class="col"><h4>Resources</h4><a href="#">Curabitur</a><a href="#">Pellentesque risus</a><a href="#">Dolupis</a><a href="#">Placerat</a></div>
  <div class="newsletter">
    <h4>Newsletter Subscribe</h4>
    <p>Curabitur pellentesque risus dui, quis placerat</p>
    <div class="subscribe"><span>Enter Email Address</span><b><svg width="10" height="14" viewBox="0 0 10 14"><path d="M2 1l6 6-6 6" fill="none" stroke="#fff" stroke-width="2.5"/></svg></b></div>
    <div class="icons"><i></i><i></i><i></i><i></i><i></i></div>
    <div class="cards"><i></i><i></i><i></i><i></i><i></i></div>
  </div>
</footer>
<div class="copyright">Copyright © 2019 - Company Name. All Right Reserved</div>
</body>
</html>
```